Bright maple lantern with an elephant incorporated in the background

Target Market(s)

Real estate

Industry/Entity Type

Real Estate

Contact Information for Business Card

On back on want my name & number
In front I want the business name, "bright maple lantern", below to say staging & design

Logo Text

Bright maple lantern

Font styles to use
Serif

Colors
000000

Requirements
Must have
• I want an elephant behind the writing in gold transperant

```html
<!DOCTYPE html>
<html lang="en">
<head>
<meta charset="utf-8">
<title>Bright Maple Lantern – Business Cards</title>
<link rel="stylesheet" href="https://fonts.googleapis.com/css2?family=Raleway:wght@400;500&family=Open+Sans:wght@400;500&display=swap">
<style>
  :root {
    --backdrop: #3f403d;
    --backdrop-dark: #2c2d2b;
    --card-light: #f4f3f0;
    --card-dark: #111110;
    --gold: #b8953a;
    --gold-soft: #a88a3e;
  }
  * { box-sizing: border-box; margin: 0; padding: 0; }
  html, body { width: 1200px; height: 1200px; overflow: hidden; }
  body {
    background: radial-gradient(circle at 50% 45%, var(--backdrop) 0%, var(--backdrop-dark) 90%);
    position: relative;
  }
  .card {
    position: absolute;
    left: 220px;
    width: 760px;
    height: 434px;
    border-radius: 3px;
    box-shadow: 0 14px 30px rgba(0,0,0,0.35);
  }
  .card--front { top: 140px; background: var(--card-light); }
  .card--back  { top: 630px; background: var(--card-dark); }

  .brand {
    position: absolute;
    text-align: center;
    font-family: "Raleway", sans-serif;
    color: var(--gold);
  }
  .brand__mark {
    display: block;
    width: 18px; height: 18px;
    border-radius: 50%;
    background: var(--gold);
    margin: 0 auto 16px;
  }
  .brand__name { font-weight: 500; letter-spacing: 0.12em; text-transform: uppercase; white-space: nowrap; }
  .brand__tagline { font-weight: 500; letter-spacing: 0.42em; text-transform: uppercase; margin-top: 6px; }

  .card--front .brand { left: 50px; top: 168px; width: 360px; }
  .card--front .brand__name { font-size: 22px; }
  .card--front .brand__tagline { font-size: 12px; }

  .contact {
    position: absolute;
    left: 460px; top: 140px;
    font-family: "Open Sans", sans-serif;
    color: var(--gold);
  }
  .contact__name { font-size: 28px; font-weight: 500; }
  .contact__title { font-size: 14px; margin-top: 4px; margin-left: 12px; }
  .contact__list { list-style: none; margin-top: 26px; margin-left: 12px; }
  .contact__item { display: flex; align-items: center; gap: 14px; font-size: 16px; margin-bottom: 10px; }
  .contact__icon { width: 18px; height: 18px; flex: none; }

  .card--back .brand { left: 0; right: 0; top: 170px; }
  .card--back .brand__name { font-size: 34px; font-weight: 400; letter-spacing: 0.1em; }
  .card--back .brand__tagline { font-size: 17px; color: var(--gold-soft); letter-spacing: 0.5em; }
</style>
</head>
<body>
  <section class="card card--front" aria-label="Business card front">
    <div class="brand">
      <span class="brand__mark" aria-hidden="true"></span>
      <p class="brand__name">Bright Maple Lantern</p>
      <p class="brand__tagline">Staging &amp; Design</p>
    </div>
    <div class="contact">
      <p class="contact__name">Your Name</p>
      <p class="contact__title">Job Title</p>
      <ul class="contact__list">
        <li class="contact__item">
          <svg class="contact__icon" viewBox="0 0 24 24" aria-hidden="true">
            <path fill="#b8953a" d="M6.6 10.8a15 15 0 0 0 6.6 6.6l2.2-2.2a1 1 0 0 1 1-.25 11.4 11.4 0 0 0 3.6.57 1 1 0 0 1 1 1V20a1 1 0 0 1-1 1A17 17 0 0 1 3 4a1 1 0 0 1 1-1h3.5a1 1 0 0 1 1 1c0 1.25.2 2.45.57 3.6a1 1 0 0 1-.25 1z"/>
          </svg>
          <span>000 000 0000</span>
        </li>
        <li class="contact__item">
          <svg class="contact__icon" viewBox="0 0 24 24" aria-hidden="true">
            <rect x="2" y="5" width="20" height="14" rx="1" fill="#b8953a"/>
            <path d="M2.5 5.5 12 13l9.5-7.5" fill="none" stroke="#f4f3f0" stroke-width="1.4"/>
          </svg>
          <span>youremail@xyz.com</span>
        </li>
      </ul>
    </div>
  </section>

  <section class="card card--back" aria-label="Business card back">
    <div class="brand">
      <p class="brand__name">Bright Maple Lantern</p>
      <p class="brand__tagline">Staging &amp; Design</p>
    </div>
  </section>
</body>
</html>
```